【業務の内容】
建物(鉄筋(鉄骨)コンクリート躯体)の寿命が、あとどれくらい
残っているのか(=寿命)を評価する業務

【なぜこの業務が必要か】
・いまお住まいのマンションの将来計画を考えるために重要な基礎資料
例えば
・「建物寿命は、あと50年以上あるので、しっかりと設備も改修しよう」
・「建物寿命は、あと50年以上あるので、耐震補強を考えよう」
・「建物寿命が20年程度しか残っていないから、延命のための改修をしよう」
・「建物寿命が20年程度しか残っていないから、建替えの検討をしよう」
・残存寿命が長いなら、耐震補強や給排水設備の改修、共用部のリニューアル等を
実施する価値がある、と判断できる

【この業務を推す背景】
・築30年、40年を超える高経年マンションが増えてきている
・首都圏では大地震の確率が30年以内に70%と言われており。1981年以前の旧耐震
基準の建物は、すでに築40年を超えており、耐震補強工事を行うか、建替えるかの
選択を迫られている

【業務の費用(目安・税別)】 ※あくまでも目安
・1棟当たり 基本料金300,000+コア抜き50,000/ヶ所(1フロアあたり1ヶ所)

例)5階建て1棟のマンションの場合
基本料金300,000+(50,000×5ヶ所)=550,000(税別)
【訴求したい事】
・建物の寿命評価に特化しているので、耐震診断等と比べて比較的
安価に実施できる
・短期間で結果が分かる(着手後およそ1か月程度)
・これからマンションにどれだけ維持修繕や改良などの投資するかという
検討をする際の客観的裏付けのある基礎資料になる
・耐用年数は「集合住宅躯体の長期保全評価指針・同付録」(日本建築
学会)の示す算定式を使って算出する

【特に注意・留意すべき事象】
・「寿命が長い」=「安全」ではない
建物耐用年数が長くても、現在の耐震性能基準に達していなければ大地震で
大破・倒壊の危険性がある。躯体寿命と建物の安全性は全く別物
・建物の寿命と設備(給排水管や電気設備など)の寿命は別物
株式会社環創プラン 本社
〒150-0074
東京都渋谷区桜見台7-13-6朝陽ビル
TEL:03-6928-4171(代)
FAX:03-6928-4178

西日本支社
大阪事務所
〒530-0086
大阪府大阪市北区松風町 6-3-18 青葉セントラルビル
TEL:06-6384-2051
FAX:06-6384-2052

西日本支社
広島事務所
〒730-0094
広島県広島市中区千草通3-8-12浜辺ビル5F
TEL:082-517-6820
FAX:082-517-6829
A4
両面
赤系、緑系、水色系
• 高解像度JPG (.jpg)
• イラストレーター形式 (.ai)
使用可能な画像、図(こちらもチラシ作成上に入れてほしいがわかりやすくいじってもらってOKです)、会社ロゴ等全て添付します。

業界関係者ではなく、一般のかた(いわゆる「素人」)が、パッとみてどう感じるだろうか、という
目線で選定しました。
・あまり小難しい印象は与えず、明快なデザイン
・「マンション販売のチラシ」や「水道修理業者」と勘違いされない
というようなところで差がありました。

はじめてこのワークバザールを利用したのですが、このように色々なご提案をいただき、
正直、驚き(もちろん嬉しい方です)でした。
やはりプロにお任せするだけのことがあると痛感し、
我々の業務も同じような驚きをお客様にお届けできるように心がけたいと思います。

この度はご提案いただきまして、誠にありがとうございました。

```html
<!DOCTYPE html>
<html lang="ja">
<head>
<meta charset="utf-8">
<title>マンション向け 建物耐用年数評価</title>
<link href="https://fonts.googleapis.com/css2?family=Noto+Sans+JP:wght@400;500;700;900&display=swap" rel="stylesheet">
<style>
:root{
  --green:#5aaf32;
  --green-dark:#2f7d2a;
  --green-pale:#e6f3dc;
  --orange:#ef8f1c;
  --orange-pale:#fdeedb;
  --sky:#bfe5f4;
  --sky-deep:#8fd0ea;
  --ink:#333;
  --gray:#5d6266;
  --cream:#f6f1e4;
}
*{margin:0;padding:0;box-sizing:border-box}
html,body{width:846px;height:1200px;overflow:hidden;background:#fff}
body{font-family:"Noto Sans JP",sans-serif;color:var(--ink);position:relative}
.abs{position:absolute}
.header{left:0;top:0;width:846px;height:160px;background:linear-gradient(180deg,var(--sky-deep),var(--sky) 70%,#fff)}
.bldg{top:0;height:160px;background:linear-gradient(180deg,#9eb7c6,#c9d9e2)}
.bldg-l{left:0;width:130px}
.bldg-r{right:0;width:150px}
.title-sub{left:50%;transform:translateX(-50%);top:18px;background:var(--green);color:#fff;font-weight:700;font-size:30px;padding:2px 40px;border-radius:4px;letter-spacing:.12em}
.title-main{left:0;width:846px;top:62px;text-align:center;font-weight:900;font-size:62px;color:#fff;letter-spacing:.06em;text-shadow:0 0 4px var(--green-dark),2px 2px 0 var(--green-dark)}
.intro{left:70px;width:706px;top:188px;text-align:center;font-size:17px;line-height:1.75;font-weight:500}
.intro em{font-style:normal;color:var(--green-dark);font-weight:700}
.flow-head{left:0;width:846px;top:300px;text-align:center;color:var(--green);font-size:30px;font-weight:500;font-style:italic}
.flow-head::before,.flow-head::after{content:"";display:inline-block;width:280px;height:1px;background:var(--green);vertical-align:middle;margin:0 20px}
.flow-sub{left:0;width:846px;top:344px;text-align:center;font-size:16px;font-weight:700}
.node{display:flex;align-items:center;justify-content:center;font-weight:700;color:#fff;font-size:17px}
.life{left:323px;top:374px;width:200px;height:36px;background:var(--green-dark)}
.branch-long{left:60px;top:428px;width:340px;height:32px;background:var(--green)}
.branch-short{left:445px;top:428px;width:340px;height:32px;background:var(--orange)}
.plan{left:373px;top:468px;width:100px;text-align:center;font-size:15px;font-weight:700}
.col{top:498px;width:170px;height:114px;padding:10px 14px;font-size:14px;line-height:1.85;font-weight:500}
.col ul{list-style:none}
.col li::before{content:"■";font-size:11px;margin-right:6px}
.c1{left:60px;background:var(--green-pale)}
.c1 li::before{color:var(--green)}
.c2{left:245px;background:var(--cream);display:flex;align-items:center;justify-content:center;text-align:center;line-height:1.5}
.c2 small{font-size:11px}
.c3{left:430px;background:var(--orange-pale)}
.c3 li::before{color:var(--orange)}
.c4{left:615px;background:var(--orange-pale)}
.c4 li::before{color:var(--orange)}
.verdict{top:622px;font-size:18px;font-weight:900}
.v-long{left:60px;color:var(--green)}
.v-short{left:420px;color:var(--orange)}
.scene{left:60px;top:656px;width:726px;height:160px;background:linear-gradient(180deg,#f4f6f2,#e3ebe0);border-radius:6px}
.word{top:676px;font-size:30px;font-weight:900;color:#7a7f82}
.bubble{width:90px;height:90px;border-radius:50%;border:2px solid var(--green);background:#fff;display:flex;align-items:center;justify-content:center;text-align:center;font-size:11.5px;font-weight:700;line-height:1.45;color:var(--green-dark)}
.bubble.o{border-color:var(--orange);color:#c06a0a}
.conclusion{left:60px;width:726px;top:828px;font-size:19px;font-weight:900;line-height:1.6}
.point-tag{left:0;top:902px;width:190px;height:36px;background:var(--green);color:#fff;font-size:24px;font-weight:700;font-style:italic;padding-left:60px;clip-path:polygon(0 0,88% 0,100% 50%,88% 100%,0 100%)}
.points{left:60px;top:946px;width:440px;font-size:11.5px;line-height:1.45}
.points li{list-style:none;margin-bottom:5px;padding-left:16px;position:relative}
.points li::before{content:"◆";position:absolute;left:0;color:var(--green)}
.points b{color:var(--green-dark)}
.points b.red{color:#d6432f}
.people{left:520px;top:902px;width:266px;height:146px;background:linear-gradient(180deg,#eef1ef,#d9dfdc);border-radius:6px}
.check-bar{left:0;top:1062px;width:846px;height:38px;background:var(--gray)}
.check-tag{left:0;top:1058px;width:190px;height:46px;background:#3f4346;color:#fff;font-size:25px;font-weight:700;font-style:italic;padding:4px 0 0 60px;clip-path:polygon(0 0,88% 0,100% 50%,88% 100%,0 100%)}
.check-q{left:210px;top:1068px;color:#fff;font-size:18px;font-weight:700}
.check-text{left:60px;width:726px;top:1112px;font-size:11.5px;line-height:1.55}
</style>
</head>
<body>
<div class="abs header"></div>
<div class="abs bldg bldg-l" role="img" aria-label="マンション外観のイラスト"></div>
<div class="abs bldg bldg-r" role="img" aria-label="高層マンション外観のイラスト"></div>
<div class="abs title-sub">マンション向け</div>
<h1 class="abs title-main">建物耐用年数評価</h1>

<p class="abs intro"><em>建物耐用年数評価</em>とは、建物(鉄筋(鉄骨)コンクリート躯体)の寿命が、<br>あとどれくらい残っているのか(=寿命)を評価する業務です。<br><em>いまお住まいのマンションの将来計画を考えるために重要な基礎資料</em>となります。</p>

<div class="abs flow-head">Flow</div>
<div class="abs flow-sub">建物耐用年数評価から将来を計画する時の流れ</div>

<svg class="abs" style="left:0;top:0" width="846" height="520" aria-hidden="true">
  <g stroke="#8a8f92" stroke-width="2" fill="none">
    <path d="M423 410 V420 M230 420 H615 M230 420 V428 M615 420 V428"/>
    <path d="M145 460 V498 M330 460 V498 M515 460 V498 M700 460 V498"/>
  </g>
</svg>
<div class="abs node life">建物の寿命</div>
<div class="abs node branch-long">残存寿命が長い</div>
<div class="abs node branch-short">残存寿命が短い</div>
<div class="abs plan">将来計画</div>

<div class="abs col c1"><ul><li>耐震診断・補強</li><li>設備更新</li><li>大規模修繕</li><li>改良・改修</li></ul></div>
<div class="abs col c2"><div>スーパーリフォーム<br><small>(スケルトンリフォーム)</small></div></div>
<div class="abs col c3"><ul><li>コンクリート改修</li><li>耐震診断・補強</li><li>設備更新</li><li>大規模修繕</li></ul></div>
<div class="abs col c4"><ul><li>建替え</li><li>敷地売却</li></ul></div>

<div class="abs verdict v-long">建物寿命はあと 50 年以上ある</div>
<div class="abs verdict v-short">建物寿命が 20 年程度しか残っていない</div>

<div class="abs scene" role="img" aria-label="将来計画を話し合う住民たちのイラスト"></div>
<div class="abs word" style="left:90px">対策</div>
<div class="abs word" style="left:385px;top:752px">検討</div>
<div class="abs word" style="left:690px">改善</div>
<div class="abs bubble" style="left:185px;top:720px">耐震補強を<br>考えよう</div>
<div class="abs bubble" style="left:260px;top:664px">しっかりと設備<br>も改修しよう</div>
<div class="abs bubble o" style="left:490px;top:664px">建替えの<br>検討を<br>しよう</div>
<div class="abs bubble o" style="left:565px;top:720px">延命のための<br>改修をしよう</div>

<p class="abs conclusion">建物耐用年数評価によって、残存寿命が長いなら耐震補強や給排水設備の改修、共用部のリニューアル等を実施する価値があると、判断できます。</p>

<div class="abs point-tag">Point</div>
<ul class="abs points">
  <li><b class="red">「寿命が長い」≠「安全」ではありません。</b><br>建物耐用年数が長くても、現在の耐震性能基準に達していなければ大地震で大破・倒壊の危険性があります。躯体寿命と建物の安全性は全く別物です。</li>
  <li><b>建物の寿命と設備(給排水管や電気設備など)の寿命は別物です。</b></li>
</ul>
<div class="abs people" role="img" aria-label="管理組合のメンバーのイラスト"></div>

<div class="abs check-bar"></div>
<div class="abs check-tag">Check!</div>
<div class="abs check-q">あなたのマンション、築年数はどのくらい?</div>
<p class="abs check-text">昨今では築30年、40年を超える高経年マンションが増えてきています。首都圏では大地震の確率が30年以内に70%と言われており、1981年以前の旧耐震基準の建物は、すでに築40年を超え、耐震補強工事を行うか、建替えるかの選択を迫られています。<br>裏面では建物耐用年数評価について詳しくご紹介しております。</p>
</body>
</html>
```